Unique Realty Niche needs a web design

Starting Note: Please do not use the colors from the logo on keyplotmeadowdoors.example which is their current website. This logo will eventually change but it is what they have now.

This website is a realty website that caters to individuals who want to rent out their homes (investors) and those who want to rent a home (Tenants). We provide no credit check to rent a home from a investor at a higher cost for the tenant to balance risk. Good renters with bad credit are able to rent or buy a house from investors who are registered in our system.

Target Market(s)

Home Owners trying to rent out their homes, and people looking to rent.

Industry/Entity Type

House

Requirements
Must have
• Main Navigation links: Home - Our Story - tenant - owner - contact us

A log in form somewhere on the page.

Key themes in the site are as follows: The site needs to be clean and professional looking i.e. no grunge. I provided some color palettes below, these are not set in stone and if you know of a good palette(s) our client is very open to all suggestions. The main navigation needs to stay on top but other on page navigations could go on left (preferably) On the left or the right will be featured listings for some homes. It will be between 3 to 5 listings showing at one time. (Please see keyplotmeadowdoors.example for example)

Example Color Palettes:
http://hueboard.example/#themeID/1000001
http://hueboard.example/#themeID/100002
http://hueboard.example/#themeID/1000003
http://hueboard.example/#themeID/1000004

Example Websites That Client Likes:
NOTE: Very Flexible, no need to duplicate these below.
http://www.lanternestatesgrove.example/
http://www.vkhquarry.example/
http://www.tufelbrookstewards.example/index.php?pr=Home_Page

Nice to have
• It would be nice to have short easy to read paragraphs accompanied by a photo so scanning is easy on the site. Then in later pages we will have more text when there is more detail needed. We know you wont come up with the content but concept would be nice.

```html
<!DOCTYPE html>
<html lang="en">
<head>
<meta charset="utf-8">
<title>Keyplot Meadow Doors</title>
<link rel="stylesheet" href="https://fonts.googleapis.com/css2?family=Arimo:ital,wght@0,400;0,700;1,400&display=swap">
<style>
:root{
  --ink:#333;
  --text:#555;
  --muted:#888;
  --line:#ddd;
  --nav-top:#9aab97;
  --nav-bottom:#66795f;
  --teal:#76b3ad;
  --teal-soft:#cfe8ea;
  --orange:#f47b20;
  --red:#d7322f;
  --paper:#fff;
  --black:#111;
}
*{box-sizing:border-box;margin:0;padding:0}
html,body{width:1200px;height:2400px;overflow:hidden;background:var(--paper)}
body{font-family:"Arimo",Arial,sans-serif;color:var(--text);position:relative}
.page{position:relative;width:1200px;height:2400px;border-top:3px solid var(--ink)}
.abs{position:absolute}

/* header */
.utility{top:8px;left:965px;font-size:12px;color:var(--ink);display:flex;gap:22px}
.utility span::before{content:"•";margin-right:4px;color:var(--muted)}
.brand{top:30px;left:60px;display:flex;align-items:center;gap:26px}
.brand-mark{width:48px;height:48px;background:var(--teal);border-radius:50%}
.brand-name{font-size:45px;color:var(--text);letter-spacing:-.5px}
.phone-icon{top:56px;left:963px}
.phones{top:56px;left:1017px;font-size:17px;color:var(--ink);line-height:25px}

.mainnav{top:115px;left:46px;width:1108px;height:45px;border-radius:10px;
  background:linear-gradient(var(--nav-top),var(--nav-bottom));border:1px solid #5d6d58}
.mainnav a{position:absolute;top:12px;color:#fff;font-size:18px;text-decoration:none;text-transform:uppercase}
.mainnav a::before{content:"›";color:#d8e2d4;margin-right:6px}
.nav-search-label{position:absolute;left:836px;top:13px;font-size:15px;font-style:italic;color:var(--ink)}
.nav-search-input{position:absolute;left:896px;top:11px;width:164px;height:22px;background:#fff;border:1px solid #aaa}
.nav-go{position:absolute;left:1070px;top:10px;width:24px;height:24px;border-radius:50%;background:#444;color:#fff;font-size:9px;text-align:center;line-height:24px}

/* side panels */
.panel-label{font-size:21px;font-style:italic;color:var(--text)}
.panel{border:2px solid #bbb;border-radius:10px;background:#fff}
.search-panel{top:302px;left:33px;width:252px;height:212px}
.search-title{position:absolute;top:14px;left:12px;font-size:20px;color:var(--ink)}
.search-sep{position:absolute;top:46px;left:12px;right:12px;border-top:1px dashed #ccc}
.field-label{position:absolute;left:16px;width:96px;height:18px;background:var(--teal-soft);font-size:12px;text-align:center;line-height:18px;color:var(--ink)}
.radio{position:absolute;top:59px;font-size:12px;color:var(--ink)}
.radio i{display:inline-block;width:10px;height:10px;border:1px solid #888;border-radius:50%;margin-right:4px;vertical-align:-1px}
.radio i.on{background:radial-gradient(#333 35%,#fff 45%)}
.select{position:absolute;left:120px;width:112px;height:19px;border:1px solid #999;font-size:12px;padding-left:4px;line-height:17px;color:var(--ink)}
.select::after{content:"▾";position:absolute;right:4px;top:0;font-size:11px}
.btn-gray{position:absolute;background:linear-gradient(#aaa,#777);color:#fff;font-size:12px;text-align:center;border:1px solid #666;border-radius:2px}

.hero{top:219px;left:310px;width:564px;height:343px;border:6px solid #d8d8d8;border-radius:30px;overflow:hidden;background:#fff}
.bubble{position:absolute;top:18px;left:22px;width:142px;height:60px;background:var(--black);border-radius:50%;color:#fff;font-size:19px;text-align:center;line-height:60px}
.bubble-tail{position:absolute;top:68px;left:90px}
.hero-name{position:absolute;top:92px;left:104px;font-size:30px;color:var(--black);letter-spacing:-.5px}
.hero-offer{position:absolute;top:150px;left:78px;font-size:34px;color:var(--orange);letter-spacing:-1px}
.hero-address{position:absolute;top:213px;left:30px;font-size:17px;color:var(--ink)}
.hero-house{position:absolute;top:40px;left:285px;width:275px;height:230px;background:linear-gradient(#e8eef3,#cfd6dc 60%,#8aa36a)}
.hero-grass{position:absolute;left:0;right:0;bottom:0;height:96px;background:linear-gradient(#c7e08a,#6fa335)}
.dots{position:absolute;left:399px;top:298px;display:flex;gap:8px}
.dots span{width:28px;height:28px;border-radius:50%;background:var(--black);color:#fff;font-size:10px;text-align:center;line-height:28px}

.login-panel{top:302px;left:895px;width:248px;height:212px}
.login-lab{position:absolute;left:17px;font-size:16px;color:var(--ink)}
.login-input{position:absolute;left:77px;width:163px;height:20px;border:1px solid #999}
.log-btn{position:absolute;left:178px;top:78px;width:62px;height:50px;background:linear-gradient(#555,#222);color:#fff;font-size:12px;text-align:center;line-height:50px;border-radius:3px}
.remember{position:absolute;left:16px;top:143px;font-size:11px;color:var(--ink)}
.remember i{display:inline-block;width:12px;height:12px;border:1px solid #888;margin-right:6px;vertical-align:-2px}
.login-sep{position:absolute;top:163px;left:14px;right:8px;border-top:2px dashed var(--teal)}

/* featured */
.section-head{top:584px;left:62px;font-size:17px;color:var(--ink);text-transform:uppercase}
.section-head::before{content:"";display:inline-block;width:11px;height:6px;background:var(--red);border-radius:3px;margin-right:12px;vertical-align:3px}
.rule{left:60px;width:1090px;border-top:1px solid #eee}
.feature-title{top:642px;left:65px;font-size:41px;font-weight:700;color:#444;letter-spacing:-1px}
.burst{top:624px;left:302px}
.old-price{top:730px;left:72px;font-size:19px;color:var(--ink)}
.new-price{top:752px;left:160px}
.feature-house{top:651px;left:280px;width:358px;height:198px;background:linear-gradient(#f4f5f7,#b7c1c9 55%,#3f5a38);border-radius:2px}
.feature-address{top:822px;left:65px;font-size:17px;font-weight:700;color:#444;line-height:23px}
.thumb{top:682px;width:146px;height:146px;background:linear-gradient(#7fa8d4,#c9d3db 45%,#7c9358)}
.thumb-cap{top:836px;width:180px;text-align:center;font-size:13px;font-weight:700;color:#444;line-height:19px}
.tag50{top:636px;left:976px;width:54px;height:54px;border-radius:50%;background:var(--black);color:#fff;font-size:15px;text-align:center;line-height:20px;padding-top:7px}

/* promo */
.holiday{top:918px;left:0;width:1200px;text-align:center;font-size:38px;color:#666;letter-spacing:1px}
.holiday .o{color:#8a9a7a}.holiday .t{color:var(--teal)}
.promo{left:0;width:1200px;text-align:center;font-size:20px;font-weight:700}
.promo.dark{top:978px;color:var(--text)}
.promo.teal{top:1012px;color:var(--teal);line-height:29px}

/* listings */
.listing-frame{top:1083px;left:46px}
.listing-head{top:1098px;left:103px;width:994px;display:flex;align-items:center;gap:12px}
.listing-head h2{font-size:20px;font-weight:400;color:var(--ink);white-space:nowrap}
.hatch{flex:1;height:12px;background:repeating-linear-gradient(90deg,#ccc 0 1px,#fff 1px 3px)}
.more{font-size:9px;color:#fff;background:#555;padding:1px 4px}
.listings{top:1131px;left:97px;width:1000px;list-style:none}
.listings li{height:28.6px;border-bottom:1px dotted #bbb;font-size:13px;line-height:28px;color:var(--text);display:flex;justify-content:space-between;padding:0 5px}
.listings li span:first-child::before{content:"•";margin-right:5px}
.flag{display:inline-block;width:11px;height:11px;background:var(--orange);border-radius:2px;margin-left:6px;vertical-align:-1px}

.legend{top:1505px;left:262px;width:672px;height:149px;border:4px solid #ddd;border-radius:24px;text-align:center;font-size:20px;color:var(--muted);line-height:29.5px;padding-top:13px}
.perks{top:1692px;left:0;width:1200px;text-align:center;font-size:20px;font-weight:700;color:var(--ink);line-height:29px;list-style:none}

/* footer */
.band{top:1981px;left:40px;width:1110px;height:8px;background:#ddd}
.check-back{top:2091px;left:130px;width:370px;text-align:center;font-size:20px;color:var(--teal);line-height:31px}
.hotline-label{top:2024px;left:734px;font-size:16px;color:var(--ink)}
.hotline{top:2048px;left:734px;font-size:36px;font-weight:700;color:var(--black);letter-spacing:-.5px}
.hotline-rule{top:2095px;left:734px;width:302px;border-top:2px solid #444}
.hotline-copy{top:2111px;left:734px;width:210px;font-size:12px;color:var(--ink);line-height:15px}
.foot-rule{left:40px;width:1110px;border-top:1px solid #ddd}
.footnav{top:2262px;left:77px;font-size:17px;color:var(--black);font-weight:700}
.footnav a{position:absolute;white-space:nowrap;color:inherit;text-decoration:none}
.footnav a::before{content:"›";margin-right:5px}
.footinfo{top:2302px;left:79px;font-size:12px;color:var(--ink);line-height:23px}
.footinfo b{font-weight:700}
.foot-brand{top:2318px;left:958px;display:flex;align-items:center;gap:8px;font-size:14px;color:var(--text)}
.foot-brand i{width:16px;height:16px;background:var(--teal);border-radius:50%}
</style>
</head>
<body>
<div class="page">

  <header>
    <div class="abs utility"><span>Log in</span><span>Join us</span><span>Site map</span></div>
    <div class="abs brand"><span class="brand-mark"></span><span class="brand-name">Keyplot Meadow Doors</span></div>
    <svg class="abs phone-icon" width="40" height="40" viewBox="0 0 40 40" aria-hidden="true">
      <path d="M4 14c0-6 32-6 32 0v4h-8v-3c-4-2-12-2-16 0v3H4z" fill="#333"/>
      <rect x="8" y="20" width="24" height="16" rx="3" fill="#444"/>
      <circle cx="20" cy="28" r="5" fill="#bbb"/>
    </svg>
    <div class="abs phones">+1 -555-014-7138<br>+1 -555-019-6043</div>

    <nav class="abs mainnav">
      <a style="left:168px">Home</a>
      <a style="left:259px">Our Story</a>
      <a style="left:400px">Tenant</a>
      <a style="left:508px">Owner</a>
      <a style="left:614px">Contact Us</a>
      <span class="nav-search-label">Search</span>
      <span class="nav-search-input"></span>
      <span class="nav-go">GO</span>
    </nav>
  </header>

  <section>
    <div class="abs panel-label" style="top:268px;left:54px">Search</div>
    <svg class="abs" style="top:266px;left:208px" width="70" height="70" viewBox="0 0 70 70" aria-hidden="true">
      <circle cx="28" cy="28" r="20" fill="#eef2f5" stroke="#555" stroke-width="5"/>
      <line x1="42" y1="42" x2="62" y2="62" stroke="#6a2d3a" stroke-width="8" stroke-linecap="round"/>
    </svg>
    <div class="abs panel search-panel">
      <div class="search-title">Search your home</div>
      <div class="search-sep"></div>
      <div class="field-label" style="top:58px">Images</div>
      <div class="radio" style="left:122px"><i class="on"></i>Y</div>
      <div class="radio" style="left:172px"><i></i>N</div>
      <div class="field-label" style="top:84px">Type</div>
      <div class="select" style="top:83px">Cottage</div>
      <div class="field-label" style="top:110px">City</div>
      <div class="select" style="top:109px"></div>
      <div class="btn-gray" style="left:56px;top:136px;width:142px;height:26px;line-height:24px">Search</div>
      <div class="btn-gray" style="left:17px;top:172px;width:220px;height:25px;line-height:23px">Advance Search</div>
    </div>

    <div class="abs hero">
      <div class="hero-house" role="img" aria-label="White two-storey cottage photo"></div>
      <div class="hero-grass" role="img" aria-label="Green lawn and grass"></div>
      <div class="bubble">850$ sqft</div>
      <svg class="bubble-tail" width="30" height="30" viewBox="0 0 30 30" aria-hidden="true"><path d="M0 0h26L6 28z" fill="#111"/></svg>
      <div class="hero-name">abc Cottage</div>
      <div class="hero-offer">Best Offer</div>
      <div class="hero-address">10521 xyz Drive Dallas, TX 12345</div>
      <div class="dots"><span>01</span><span>02</span><span>03</span><span>04</span></div>
    </div>

    <div class="abs panel-label" style="top:268px;left:913px">Log in</div>
    <div class="abs panel login-panel">
      <span class="login-lab" style="top:24px">User</span>
      <span class="login-input" style="top:24px"></span>
      <span class="login-lab" style="top:46px">Pass</span>
      <span class="login-input" style="top:46px"></span>
      <span class="log-btn">LOG</span>
      <div class="remember"><i></i>Remember me</div>
      <div class="login-sep"></div>
      <div class="btn-gray" style="left:15px;top:172px;width:222px;height:25px;line-height:23px;font-weight:700">Join us</div>
    </div>
  </section>

  <section>
    <h2 class="abs section-head" style="font-weight:400">Featured Listings</h2>
    <div class="abs rule" style="top:612px"></div>

    <div class="abs feature-house" role="img" aria-label="Large two-storey house with trees"></div>
    <div class="abs feature-title">VA COTTAGE</div>
    <svg class="abs burst" width="114" height="108" viewBox="0 0 114 108">
      <polygon fill="#555" points="57,0 66,16 82,6 84,25 103,22 97,40 114,48 99,59 108,76 89,77 88,96 71,88 62,106 52,91 37,102 33,83 14,85 20,67 3,58 18,46 9,30 27,28 28,9 44,16"/>
      <text x="57" y="50" text-anchor="middle" fill="#fff" font-family="Arimo,Arial,sans-serif" font-size="26">$100</text>
      <text x="57" y="78" text-anchor="middle" fill="#fff" font-family="Arimo,Arial,sans-serif" font-size="24">Off</text>
    </svg>
    <div class="abs old-price">1000$ sqft</div>
    <svg class="abs new-price" width="120" height="52" viewBox="0 0 120 52">
      <ellipse cx="60" cy="26" rx="56" ry="21" fill="none" stroke="#d7322f" stroke-width="2.5"/>
      <text x="60" y="32" text-anchor="middle" fill="#333" font-family="Arimo,Arial,sans-serif" font-size="19">900$ sqft</text>
    </svg>
    <div class="abs feature-address">10461 Lantern Drive Dallas,<br>TX 75229</div>

    <div class="abs thumb" style="left:655px" role="img" aria-label="Single-storey brick house photo"></div>
    <div class="abs thumb" style="left:826px" role="img" aria-label="Two-storey brick house photo"></div>
    <div class="abs thumb" style="left:998px" role="img" aria-label="Brick house with garage photo"></div>
    <div class="abs tag50">$50<br>Off</div>
    <div class="abs thumb-cap" style="left:638px">4518 Rowan<br>Drive Mesquite,<br>TX 75150</div>
    <div class="abs thumb-cap" style="left:809px">2782 Quiet Cove<br>Drive Lewisville,<br>TX 75056</div>
    <div class="abs thumb-cap" style="left:981px">1027 Fernfield<br>Drive Garland,<br>TX 75040</div>
    <div class="abs rule" style="top:917px"></div>
  </section>

  <section>
    <div class="abs holiday">HAPPY <span class="o">HOL</span><span class="t">ID</span>AYS!!!!</div>
    <div class="abs promo dark">BE IN YOUR NEW HOME BEFORE CHRISTMAS!!</div>
    <div class="abs promo teal">ASK ABOUT OUR $100 OFF SPECIAL ON SOME<br>OF OUR HOMES MARKED *** BELOW!!</div>
  </section>

  <section>
    <svg class="abs listing-frame" width="1108" height="414" viewBox="0 0 1108 414" aria-hidden="true">
      <path d="M50 3Q3 3 3 60V354Q3 411 50 411" fill="none" stroke="#76b3ad" stroke-width="6"/>
      <path d="M1058 3Q1105 3 1105 60V354Q1105 411 1058 411" fill="none" stroke="#76b3ad" stroke-width="6"/>
    </svg>
    <div class="abs listing-head"><h2>Keyplot Meadow Doors</h2><span class="hatch"></span><span class="more">MORE</span></div>
    <ul class="abs listings">
      <li><span>1027 Fernfield Dr. Garland, 75040 3/1.5/1 999 sqft. $995.00<i class="flag"></i></span><span>[07.12.21]</span></li>
      <li><span>11721 Ashby Ln. Dallas, 75128 3/1/1 1092 sqft. $995.00 ?<i class="flag"></i></span><span>[07.12.21]</span></li>
      <li><span>1107 Calle Serena Mesquite, 75149 3/2 1150 sqft. $1095.00***</span><span>[07.12.21]</span></li>
      <li><span>4518 Rowan Dr. Mesquite, 75150 3/1.5/1 1018 sqft. $1195.00***</span><span>[07.12.21]</span></li>
      <li><span>1153 Birchwood Dr. Crowley, 76036 3/2/2 1410 sqft. $1295.00***</span><span>[07.12.21]</span></li>
      <li><span>10461 Lantern Dr. Dallas, 75229 3/2/2 1392 sqft. $1295.00</span><span>[07.12.21]</span></li>
      <li><span>856 Pinto Ln. Fort Worth, 76052 3/2/2 1590 sqft. $1195.00</span><span>[07.12.21]</span></li>
      <li><span>1260 Kestrel Cr. Fort Worth, 76134 3/2/2 1380 sqft. $1295.00</span><span>[07.12.21]</span></li>
      <li><span>8502 Greyhill Ave. Dallas, 75209 2/1/1 816 sqft. $1595.00***</span><span>[07.12.21]</span></li>
      <li><span>4605 Bellamy Ct. Arlington, 76016 3/2/2 2450 sqft. $1495.00</span><span>[07.12.21]</span></li>
      <li><span>8601 Harvest Trace Ln. Plano, 75024 3/2.5/2 1585 sqft. $1595.00</span><span>[07.12.21]</span></li>
      <li><span>2828 Nightjar Dr. Mesquite, 75181 3/2/2 1876 sqft. $1895.00***</span><span>[07.12.21]</span></li>
    </ul>

    <div class="abs legend">
      (? = PROPERTIES THAT WILL BE COMING AVAILABLE SOON)<br>
      (* = DOES NOT APPLY TO ALL PROPERTIES)<br>
      (P = DEPOSIT ACCEPTED, LEASE PENDING)<br>
      ($ = ONE MONTHS FREE RENT)
    </div>

    <ul class="abs perks">
      <li>MOVE IN TODAY!!</li>
      <li>LEASE TO OWN!!</li>
      <li>FREE MONTHS RENT!!*</li>
      <li>NO CREDIT CHECKS!!</li>
      <li>NO QUALIFICATIONS!!</li>
      <li>NO APPLICATION PROCESS!!</li>
      <li>NO PET RESTRICTIONS!!*</li>
      <li>NO SMOKER RESTRICTIONS!!*</li>
    </ul>
  </section>

  <footer>
    <div class="abs band"></div>
    <div class="abs check-back">CHECK BACK FOR OUR WEEKLY<br>UPDATES AND NEW LISTINGS!!</div>
    <div class="abs hotline-label">HOT LINE</div>
    <div class="abs hotline">+1-555-091-5604</div>
    <div class="abs hotline-rule"></div>
    <p class="abs hotline-copy">Lorem ipsum dolor sit amet, consec tetuer adipiscing elit. Praesent vestibulum molestie lacus. Aenean nonummy hen drerit mauris. Phasellus porta. Fusce suscipit varius mi.</p>

    <div class="abs foot-rule" style="top:2249px"></div>
    <nav class="abs footnav">
      <a style="left:0">HOME</a>
      <a style="left:94px">OUR STORY</a>
      <a style="left:232px">TENANT</a>
      <a style="left:338px">OWNER</a>
      <a style="left:444px">CONTACT US</a>
    </nav>
    <div class="abs foot-rule" style="top:2290px"></div>
    <div class="abs footinfo">
      <b>Lorem ipsum dolor</b> | sit amet: consec | tetuer adipiscing elit.<br>
      Tel : 01-123-4567 &nbsp;/ &nbsp;Fax : &nbsp;01-234-5678 &nbsp;/ &nbsp;Email : webmaster@keyplotmeadowdoors.example<br>
      Copyright©2011. All Rights Reserved.
    </div>
    <div class="abs foot-brand"><i></i>Keyplot Meadow Doors</div>
  </footer>

</div>
</body>
</html>
```